School website design - Technology and the arts

We will need a new or updated design that incorporates the following features:
-Reactive design that changes with the needs of the device.
-Static Background - only content scrolls
-Static Menu - similar to the Pressly Harbor Lantern theme
-Alert box for important notices (closings/emergency use only) that doesn’t display unless active
-Margins must be wider than “standard pressly theme” (fits the entire display at any resolution, doesn’t just center a columned design)
-Features an image scroll on the front page to show our current works/progress. (only if the screen is big enough). Should have swipe capability
-We must have a place on the front page to display the current school news as well as a location to display current events with a poster (see current webdesign for example)
-Uses the school colors (green and gold/yellow) in a way that is pleasing to the eye.
-Unique design to our school that is very clean and modern.
-Events need to be able to pop-out when you mouseover in a desktop environment. Example: http://skinvault.example/category/pressly/creative (mouse over a theme and it shows additional information about it without a refresh)
-Custom Admin panel to easily updated the news and events section.
-Notes: We are currently using some free icons that we found to make the current site look not so boring since we do not have a lot of content on each page. We would like to step away from that and are open to suggestions. Possibly something like http://vormlab.example/demo/?theme=arch under the services section but smaller.
-Notes 2: We have plenty of pictures of our building and activities that can be used as a background, etc.
-We are open to new ideas and suggestions.

Our current website is https://www.kelmont-academy.example to get an idea on how we manage our current site.

```html
<!DOCTYPE html>
<html lang="en">
<head>
<meta charset="utf-8">
<title>Kelmont Regional Academy</title>
<link rel="stylesheet" href="https://fonts.googleapis.com/css2?family=Open+Sans:wght@400;600;700&display=swap">
<style>
:root{
  --gold:#f8c00c;
  --green:#1d5a2b;
  --green-text:#1f6a2e;
  --dark:#333333;
  --ink:#3a3a3a;
  --muted:#666666;
  --line:#d9d9d9;
  --white:#ffffff;
}
*{box-sizing:border-box;margin:0;padding:0}
html,body{width:1200px;height:900px;overflow:hidden;background:var(--white)}
body{position:relative;font-family:"Open Sans",Arial,sans-serif;color:var(--ink)}
.abs{position:absolute}
.line{display:block;white-space:nowrap;text-align:justify;text-align-last:justify}
.line.last{text-align-last:left}
.page{left:240px;top:0;width:720px;height:900px;background:var(--gold)}
.topbar{left:240px;top:0;width:720px;height:27px;background:var(--dark)}
.topbar .brand-mark{left:97px;top:5px;width:16px;height:16px;background:var(--white)}
.topbar .brand-mark::after{content:"";position:absolute;left:3px;top:3px;width:8px;height:8px;border-left:2px solid var(--dark);border-top:2px solid var(--dark);transform:rotate(-45deg) translate(2px,3px)}
.topbar .site-label{left:125px;top:9px;font-size:7px;color:#e6e6e6}
.topbar .menu-toggle{left:198px;top:5px;width:16px;height:16px;background:var(--white);padding:4px 3px;display:flex;flex-direction:column;justify-content:space-between}
.menu-toggle span{height:2px;background:var(--dark)}
.social{left:510px;top:0;display:flex;gap:1px}
.social span{width:29px;height:27px;background:#4c4c4c}
.social span:nth-child(2){background:#555}
.social span:nth-child(4){background:#5e5e5e}

.header{left:336px;top:27px;width:532px;height:64px;background:var(--white)}
.logo-dot{left:9px;top:4px;width:34px;height:34px;border-radius:50%;background:var(--green)}
.site-title{left:50px;top:15px;font-size:9.5px;font-weight:600;color:#222;white-space:nowrap}
.site-title small{font-size:6.5px;font-weight:400;color:var(--muted);margin-left:2px}
.contact{left:444px;top:11px;font-size:5.6px;color:#333;line-height:12px;white-space:nowrap}
.contact div{display:flex;align-items:center;gap:5px}
.rule{left:8px;top:38px;width:516px;height:1px;background:#ececec}
.nav{left:18px;top:47px;display:flex;font-size:6.8px;color:#444}
.nav span{margin-right:16px}
.address{left:376px;top:45px;font-size:6.5px;color:#555;display:flex;align-items:center;gap:3px;white-space:nowrap}
.green-bar{left:336px;top:91px;width:532px;height:3px;background:var(--green)}

.slider{left:336px;top:95px;width:532px;height:156px;background:linear-gradient(90deg,#b9a894 0%,#d9cdbd 35%,#e7e2d8 55%,#9aa98a 80%,#d8d2c4 100%)}
.slider-arrow{top:60px;width:22px;height:33px;background:#3b3b3b;display:flex;align-items:center;justify-content:center}
.slider-arrow.prev{left:0}.slider-arrow.next{right:0}

.features{left:336px;top:254px;width:532px;height:75px;background:var(--white);display:flex}
.feature{position:relative;flex:1;padding:10px 0 0 36px}
.feature svg{position:absolute;left:6px;top:11px}
.feature h3{font-size:11.5px;font-weight:400;color:#333;margin-bottom:4px}
.feature p{font-size:8px;line-height:12.5px;color:#444;width:134px}
.features-bar{left:336px;top:329px;width:532px;height:3px;background:var(--green)}

.panel{background:var(--white)}
.welcome{left:336px;top:345px;width:373px;height:121px}
.welcome .photo{left:8px;top:8px;width:150px;height:105px;background:linear-gradient(135deg,#d6cfc4,#6c6f78 60%,#3b4a66)}
.welcome h2{left:166px;top:5px;font-size:12.5px;font-weight:600;color:var(--green-text)}
.welcome p{left:166px;top:21px;width:198px;font-size:8px;line-height:12.7px;color:#444;text-align:justify}
.btn{display:flex;align-items:center;gap:9px;padding-left:6px;font-size:8px;color:#333;border:1px solid #ddd;border-bottom:2px solid var(--green);background:var(--white)}
.welcome .btn{left:166px;top:89px;width:88px;height:24px}

.news{left:336px;top:467px;width:223px;height:250px}
.news-tab{left:0;top:9px;width:212px;height:20px;background:var(--gold);display:flex;align-items:center;gap:9px;padding-left:3px;color:var(--white);font-size:9.5px}
.news-item{left:8px;width:210px;height:62px}
.news-item .photo{left:0;top:0;width:92px;height:60px;background:linear-gradient(135deg,#cdbfae,#7d6c5f 55%,#3e3a3a)}
.news-item h4{left:95px;top:1px;font-size:9px;font-weight:600;color:var(--green-text);white-space:nowrap}
.news-item p{left:96px;top:16px;width:114px;font-size:7.6px;line-height:12.5px;color:#555;text-align:justify}
.news-sep{left:100px;width:117px;height:1px;background:#e3e3e3}

.testimonials{left:561px;top:467px;width:148px;height:250px}
.testimonials h3{left:45px;top:13px;font-size:10px;font-weight:400;color:#333}
.t-rule{left:5px;top:28px;width:134px;height:2px;background:var(--dark)}
.quote{left:6px;font-family:Georgia,serif;font-size:24px;font-weight:700;color:#444;line-height:1}
.t-text{left:29px;width:108px;font-size:6.9px;line-height:10.3px;color:#555;text-align:justify}
.avatar{left:7px;width:32px;height:29px;border:1px solid #ddd;background:linear-gradient(#d7c8b0,#6b4f3a)}
.t-name{left:43px;font-size:6.8px;line-height:10px;color:#333}
.t-name span{color:#777}
.col-sep{left:559px;top:467px;width:2px;height:250px;background:#e6e6e6}
.bottom-sep{left:336px;top:717px;width:373px;height:10px;background:#f1f1f1}

.mission-title{left:336px;top:731px;display:flex;align-items:center;gap:9px;color:var(--white);font-size:9.5px}
.mission{left:336px;top:751px;width:373px;height:75px}
.mission p{left:9px;top:6px;width:355px;font-size:7.8px;line-height:12.5px;color:#444;text-align:justify}
.mission .btn{left:8px;top:47px;width:78px;height:20px}

.sidebar{left:724px;top:345px;width:144px;height:481px}
.side-h{left:6px;display:flex;align-items:center;gap:7px;font-size:9px;color:#222;width:132px;padding-bottom:2px;border-bottom:2px solid var(--dark)}
.search{left:6px;top:34px;width:133px;height:24px;border:1px solid #ddd;font-size:7.5px;color:#aaa;padding:7px 8px}
.facilities{left:6px;top:88px;font-size:6.8px;line-height:13.5px;color:#333;list-style:none}
.facilities li::before{content:"+";color:#777;margin-right:5px}
.side-p{left:7px;width:131px;font-size:6.5px;line-height:10.3px;color:#444}
.supporter-logo{left:7px;top:367px;width:41px;height:41px;border:1px solid #ddd;display:flex;align-items:center;justify-content:center}
.supporter-logo span{width:26px;height:26px;border-radius:50%;background:var(--green)}
.sidebar .btn{left:32px;top:453px;width:78px;height:20px}

.footer{left:240px;top:840px;width:720px;height:60px;background:var(--dark);color:var(--white);text-align:center;font-size:8.4px;line-height:16px;padding-top:5px}
.footer nav span{margin:0 4px}
</style>
</head>
<body>
<div class="abs page"></div>

<header class="abs topbar">
  <div class="abs brand-mark"></div>
  <div class="abs site-label">My School</div>
  <div class="abs menu-toggle"><span></span><span></span><span></span></div>
  <div class="abs social" aria-label="Social links"><span></span><span></span><span></span><span></span></div>
</header>

<div class="abs header">
  <div class="abs logo-dot"></div>
  <div class="abs site-title">Kelmont Regional Academy <span style="font-weight:400;color:#555">|</span> <small>for the arts &amp; technology</small></div>
  <div class="abs contact">
    <div><svg width="6" height="6" viewBox="0 0 10 10"><path d="M2 1l2 2-1 1.5c.8 1.5 1.5 2.2 3 3L7.5 6l2 2-1.5 1.5C4 9 1 6 .5 1.5z" fill="#333"/></svg>+1 555-014-2290</div>
    <div><svg width="6" height="5" viewBox="0 0 10 8"><rect width="10" height="8" fill="#333"/><path d="M0 0l5 4 5-4" stroke="#fff" fill="none"/></svg>office@kelmont.example</div>
  </div>
  <div class="abs rule"></div>
  <nav class="abs nav"><span>Home</span><span>Blog</span><span>Portfolio</span><span>Pages</span><span>Features</span><span>Contact</span></nav>
  <div class="abs address"><svg width="7" height="10" viewBox="0 0 10 14"><path d="M5 0a5 5 0 0 1 5 5c0 4-5 9-5 9S0 9 0 5a5 5 0 0 1 5-5z" fill="#444"/><circle cx="5" cy="5" r="2" fill="#fff"/></svg>48 Linden Ave, 20410 555.018.3300</div>
</div>
<div class="abs green-bar"></div>

<section class="abs slider" role="img" aria-label="Slideshow photo of a smiling student in a library">
  <div class="abs slider-arrow prev"><svg width="10" height="16" viewBox="0 0 10 16"><path d="M8 1L2 8l6 7" stroke="#fff" stroke-width="2" fill="none"/></svg></div>
  <div class="abs slider-arrow next"><svg width="10" height="16" viewBox="0 0 10 16"><path d="M2 1l6 7-6 7" stroke="#fff" stroke-width="2" fill="none"/></svg></div>
</section>

<section class="abs features">
  <div class="feature">
    <svg width="22" height="20" viewBox="0 0 22 20"><rect x="1" y="3" width="16" height="14" fill="none" stroke="#444" stroke-width="1.5"/><path d="M1 7h16M5 1v4M13 1v4" stroke="#444" stroke-width="1.5"/><circle cx="16" cy="14" r="5" fill="#fff" stroke="#444" stroke-width="1.5"/><path d="M16 11v3h2" stroke="#444"/></svg>
    <h3>Easy to Start</h3>
    <p><span class="line">Vela Solid provides unique mecha-</span><span class="line">nism of installing sample data on di-</span><span class="line last">rectly your current website.</span></p>
  </div>
  <div class="feature">
    <svg width="22" height="20" viewBox="0 0 22 20"><ellipse cx="9" cy="8" rx="8" ry="6" fill="#444"/><path d="M4 12l-2 5 5-3z" fill="#444"/><ellipse cx="15" cy="12" rx="6" ry="4.5" fill="#444" stroke="#fff"/></svg>
    <h3>Easy to Start</h3>
    <p><span class="line">Vela Solid provides unique mecha-</span><span class="line">nism of installing sample data on di-</span><span class="line last">rectly your current website.</span></p>
  </div>
  <div class="feature">
    <svg width="22" height="20" viewBox="0 0 22 20"><circle cx="11" cy="9" r="8" fill="none" stroke="#444" stroke-width="1.5"/><circle cx="11" cy="9" r="4" fill="#444"/><path d="M2 19h18" stroke="#444" stroke-width="2"/></svg>
    <h3>Easy to Start</h3>
    <p><span class="line">Vela Solid provides unique mecha-</span><span class="line">nism of installing sample data on di-</span><span class="line last">rectly your current website.</span></p>
  </div>
</section>
<div class="abs features-bar"></div>

<section class="abs panel welcome">
  <div class="abs photo" role="img" aria-label="Photo of a student writing in a classroom"></div>
  <h2 class="abs">Welcome To Our School</h2>
  <p class="abs">Lorem Ipsum is simply dummy text of the printing and typesetting industry. Lorem Ipsum has been the industry's standard dummy text ever since the 1500s, when an unknown printer took a galley of type and scrambled.</p>
  <div class="abs btn"><svg width="12" height="10" viewBox="0 0 12 10"><rect x="1" y="1" width="10" height="6" fill="none" stroke="#333"/><path d="M4 9h4M6 7v2" stroke="#333"/></svg>Take a tour</div>
</section>

<section class="abs panel news">
  <div class="abs news-tab"><svg width="14" height="12" viewBox="0 0 14 12"><path d="M1 7l9-6v10L1 7z" fill="#fff"/><path d="M3 8l1 4" stroke="#fff" stroke-width="1.5"/></svg>News and Events</div>
  <article class="abs news-item" style="top:38px">
    <div class="abs photo" role="img" aria-label="Photo of students studying together"></div>
    <h4 class="abs">Lorem Ipsum Text Goes</h4>
    <p class="abs">Lorem Ipsum is simply dummy text of the printing and typeset­ting industry.</p>
  </article>
  <div class="abs news-sep" style="top:102px"></div>
  <article class="abs news-item" style="top:107px">
    <div class="abs photo" role="img" aria-label="Photo of students around a laptop"></div>
    <h4 class="abs">Lorem Ipsum Text Goes</h4>
    <p class="abs">Lorem Ipsum is simply dummy text of the printing and typeset­ting industry.</p>
  </article>
  <div class="abs news-sep" style="top:172px"></div>
  <article class="abs news-item" style="top:177px">
    <div class="abs photo" role="img" aria-label="Photo of students working at a desk"></div>
    <h4 class="abs">Lorem Ipsum Text Goes</h4>
    <p class="abs">Lorem Ipsum is simply dummy text of the printing and typeset­ting industry.</p>
  </article>
</section>

<div class="abs col-sep"></div>

<section class="abs panel testimonials">
  <svg class="abs" style="left:16px;top:11px" width="18" height="16" viewBox="0 0 18 16"><circle cx="9" cy="4" r="3" fill="#444"/><circle cx="3.5" cy="9" r="2.5" fill="#444"/><circle cx="14.5" cy="9" r="2.5" fill="#444"/><path d="M5 16c0-4 8-4 8 0z" fill="#444"/></svg>
  <h3 class="abs">Testimonials</h3>
  <div class="abs t-rule"></div>
  <div class="abs quote" style="top:42px">&ldquo;</div>
  <p class="abs t-text" style="top:41px">Lorem Ipsum is simply dummy text of the printing and typeset­ting industry. Lorem Ipsum has been the industry's standard dummy text ever since the 1500s.</p>
  <div class="abs avatar" style="top:101px" role="img" aria-label="Student portrait"></div>
  <p class="abs t-name" style="top:106px">Lorem Ipsum<br><span>Student</span></p>
  <div class="abs quote" style="top:140px">&ldquo;</div>
  <p class="abs t-text" style="top:139px">Lorem Ipsum is simply dummy text of the printing and typeset­ting industry. Lorem Ipsum has been the industry's standard dummy text ever since the 1500s.</p>
  <div class="abs avatar" style="top:198px" role="img" aria-label="Student portrait"></div>
  <p class="abs t-name" style="top:204px">Lorem Ipsum<br><span>Student</span></p>
</section>
<div class="abs bottom-sep"></div>

<div class="abs mission-title"><svg width="16" height="16" viewBox="0 0 16 16"><circle cx="8" cy="8" r="2" fill="#fff"/><path d="M8 1a7 7 0 0 1 6 3.5L10 7zM2 4.5A7 7 0 0 1 8 1L6 7zM4.5 14L7 10h2l2.5 4a7 7 0 0 1-7 0z" fill="#fff"/></svg>Our Mission And Vision</div>
<section class="abs panel mission">
  <p class="abs">The Kelmont Regional Academy for the Arts and Technology provides gifted and talented students a differentiated and rigorous education, cultivates a supportive environment that inspires unique artistic and technological visions, promotes cultural tolerance.</p>
  <div class="abs btn"><svg width="10" height="11" viewBox="0 0 10 11"><rect x="1" y="1" width="8" height="9" fill="none" stroke="#333"/><path d="M3 4h4" stroke="#333"/></svg>Learn More</div>
</section>

<aside class="abs panel sidebar">
  <div class="abs side-h" style="top:6px"><svg width="11" height="11" viewBox="0 0 11 11"><circle cx="4.5" cy="4.5" r="3.5" fill="none" stroke="#333" stroke-width="1.5"/><path d="M7 7l3.5 3.5" stroke="#333" stroke-width="1.8"/></svg>Search</div>
  <div class="abs search">Search here</div>
  <div class="abs side-h" style="top:63px"><svg width="13" height="12" viewBox="0 0 13 12"><path d="M6.5 0l1.9 4 4.3.4-3.3 2.9 1 4.3-3.9-2.3-3.9 2.3 1-4.3L.3 4.4 4.6 4z" fill="#333"/></svg>Our Facilities</div>
  <ul class="abs facilities">
    <li>This is a dummy text here</li><li>This is a dummy text here</li><li>This is a dummy text here</li><li>This is a dummy text here</li><li>This is a dummy text here</li><li>This is a dummy text here</li><li>This is a dummy text here</li><li>This is a dummy text here</li><li>This is a dummy text here</li>
  </ul>
  <div class="abs side-h" style="top:211px"><svg width="10" height="10" viewBox="0 0 10 10"><path d="M2 1l2 2-1 1.5c.8 1.5 1.5 2.2 3 3L7.5 6l2 2-1.5 1.5C4 9 1 6 .5 1.5z" fill="#333"/></svg>Docs</div>
  <p class="abs side-p" style="top:232px"><span class="line">Lorem Ipsum is simply dummy text of the</span><span class="line">printing and typesetting industry. Lorem</span><span class="line">Ipsum has been the industry's standard</span><span class="line">dummy text ever since the 1500s. Lorem</span><span class="line">Ipsum is simply dummy text of the print-</span><span class="line last">ing and typesetting industry.</span></p>
  <div class="abs side-h" style="top:299px"><svg width="10" height="10" viewBox="0 0 10 10"><circle cx="5" cy="3" r="2.6" fill="#333"/><path d="M0 10c0-4 10-4 10 0z" fill="#333"/></svg>Who is online</div>
  <p class="abs side-p" style="top:320px"><span class="line">Lorem Ipsum is simply dummy text of</span><span class="line last">the printing and typesetting industry.</span></p>
  <div class="abs side-h" style="top:343px"><svg width="11" height="11" viewBox="0 0 11 11"><circle cx="5.5" cy="3" r="2.5" fill="#333"/><path d="M0 10h11v-2c-2-2-9-2-11 0z" fill="#333"/></svg>Become Our Supporter</div>
  <div class="abs supporter-logo"><span></span></div>
  <p class="abs side-p" style="top:366px;left:52px;width:86px;font-size:6.3px"><span class="line">Lorem Ipsum is simply</span><span class="line">dummy text of the printing</span><span class="line">and typesetting industry.</span><span class="line last">Lorem Ipsum has been.</span></p>
  <p class="abs side-p" style="top:409px"><span class="line">Lorem Ipsum is simply dummy text of</span><span class="line">the printing and typesetting industry.</span><span class="line last">Lorem Ipsum is simply dummy Lorem</span><span class="line last">Lorem Ipsum is simply dummy Lorem</span></p>
  <div class="abs btn"><svg width="10" height="11" viewBox="0 0 10 11"><rect x="1" y="1" width="8" height="9" fill="none" stroke="#333"/><path d="M3 4h4" stroke="#333"/></svg>Know More</div>
</aside>

<footer class="abs footer">
  <div>Copyright © 2000 - 2014 www.kelmont-academy.example</div>
  <div>All rights reserved.</div>
  <nav><span>Home</span>|<span>About us</span>|<span>Gallery</span>|<span>Our Mision</span>|<span>News and events</span>|<span>Online Availability</span>|<span>Sitemap</span>|<span>Contact Us</span></nav>
</footer>
</body>
</html>
```